Psychotherapy Practice Needs Non-Corporate Stationary

I need an elegant design for letterhead, envelope, and note card for my psychotherapy private practice in Silicon Valley. I work with pre-teens, teens, and adults primarily with anxiety, stress, and depression.

Stationary should convey warmth and professionalism. I tend to like somewhat modern designs.

My business card is already done--attached here for reference.

Target Market(s)

Professionals of Silicon Valley, Academic Advisors at High Schools, Psychologists, Psychiatrists, Pediatricians, Directors of Human Resources, Community leaders

Industry/Entity Type

Psychology

Font styles to use
Serif

Requirements
Must have
• Logo attached--can use with or without the name included. Feel free to move the name to the right of the logo. I included all versions just in case. Colors to use should match or go with the logo (greens, maybe blues if they go), but can be somewhat softer than the bold greens and browns used. (Ex. more sage green vs. kelly green)
• Letterhead--please include the following:
• Celia Montvale, LMFT
• 512 Birchwood Lane, Suite 41
• Palo Alto, CA 94303
• 650-381-7026
• celia@celiamontvale.example
• celiamontvale.example
• Envelope--please include:
• Celia Montvale, LMFT
• Palo Alto, CA 94303
• 650-381-7026
• celiamontvale.example
• Note Card--please include:
• Celia Montvale, LMFT
• 650-381-7026
• celiamontvale.example
Nice to have
• I'd love to see examples both with and without a logo watermark in the background. I especially like the watermark towards the lower right corner for the letterhead. I'd also like to see some versions of the letterhead with all contact info at the bottom.
Should not have
• It should not be corporate and should avoid harsh lines.

```html
<!DOCTYPE html>
<html lang="en">
<head>
<meta charset="utf-8">
<title>Celia Montvale, LMFT — Letterhead</title>
<link href="https://fonts.googleapis.com/css2?family=Cormorant+SC:wght@500;600&family=Open+Sans:wght@400&family=PT+Sans+Narrow:wght@700&display=swap" rel="stylesheet">
<style>
  :root {
    --backdrop: #7d7d7d;
    --paper: #f7f7f6;
    --leaf-green: #5e9a45;
    --band-green: #6c9a4c;
    --band-shadow: #4f7a36;
    --ink: #2b2b2b;
    --name-ink: #3a3a3a;
    --watermark: #e6e6e4;
  }
  * { box-sizing: border-box; margin: 0; padding: 0; }
  html, body { width: 1200px; height: 800px; overflow: hidden; }
  body { background: var(--backdrop); position: relative; font-family: "Open Sans", Arial, sans-serif; }

  .sheet {
    position: absolute; top: 83px; width: 460px; height: 645px;
    background: var(--paper); overflow: hidden;
  }
  .sheet--header { left: 90px; }
  .sheet--footer { left: 665px; }

  .brand { position: absolute; display: flex; flex-direction: column; align-items: center; }
  .brand__mark { border-radius: 50%; background: var(--leaf-green); }
  .brand__name {
    font-family: "Cormorant SC", "Times New Roman", serif; font-weight: 500;
    color: var(--name-ink); white-space: nowrap; letter-spacing: 0.1px;
  }
  .sheet--header .brand { left: 14px; top: 17px; }
  .sheet--header .brand__mark { width: 42px; height: 42px; }
  .sheet--header .brand__name { font-size: 10.5px; margin-top: 8px; }
  .sheet--footer .brand { left: 18px; top: 14px; }
  .sheet--footer .brand__mark { width: 60px; height: 60px; }
  .sheet--footer .brand__name { font-size: 14.5px; margin-top: 8px; }

  .contact-name {
    font-family: "PT Sans Narrow", "Arial Narrow", sans-serif; font-weight: 700;
    color: var(--ink); white-space: nowrap;
  }
  .contact-name .accent { color: var(--leaf-green); }

  .contact-block { position: absolute; right: 18px; top: 19px; text-align: right; }
  .contact-block .contact-name { font-size: 11px; text-transform: uppercase; margin-bottom: 7px; }
  .contact-line {
    display: flex; justify-content: flex-end; align-items: center; gap: 6px;
    font-size: 10px; color: var(--ink); line-height: 14px; white-space: nowrap;
  }
  .icon { width: 8px; height: 8px; fill: var(--leaf-green); flex: none; }

  .watermark {
    position: absolute; width: 260px; height: 280px; border-radius: 50% 50% 12% 12%;
    background: radial-gradient(ellipse at 50% 40%, var(--watermark) 0%, rgba(230,230,228,0.55) 55%, rgba(247,247,246,0) 78%);
  }
  .sheet--header .watermark { left: 200px; top: 345px; }
  .sheet--footer .watermark { left: 200px; top: 347px; }

  .base-band { position: absolute; left: 0; right: 0; bottom: 0; background: var(--band-green); border-bottom: 2px solid var(--band-shadow); }
  .sheet--header .base-band { height: 20px; }
  .sheet--footer .base-band { height: 10px; }

  .side-tab { position: absolute; left: 0; top: 132px; width: 9px; height: 88px; background: var(--band-green); }

  .footer-contacts {
    position: absolute; left: 5px; right: 7px; bottom: 13px;
    display: flex; justify-content: space-between; align-items: center;
    font-size: 10px; color: var(--ink); white-space: nowrap;
  }
  .footer-contacts .contact-name { font-size: 11px; }
  .footer-contacts .item { display: flex; align-items: center; gap: 5px; }
</style>
</head>
<body>
  <svg width="0" height="0" style="position:absolute" aria-hidden="true">
    <symbol id="icon-phone" viewBox="0 0 10 10"><path d="M2 0.5l1.6 2.2-1 1a6 6 0 0 0 3.7 3.7l1-1L9.5 8 8.3 9.5C4 9.3 0.7 6 0.5 1.7z"/></symbol>
    <symbol id="icon-web" viewBox="0 0 10 10"><circle cx="5" cy="5" r="4.5"/></symbol>
    <symbol id="icon-mail" viewBox="0 0 10 10"><rect x="0.5" y="2" width="9" height="6.5" rx="0.6"/><path d="M1 2.6l4 3 4-3" fill="none" stroke="#f7f7f6" stroke-width="0.9"/></symbol>
  </svg>

  <section class="sheet sheet--header" aria-label="Letterhead with contact details at top">
    <div class="brand">
      <span class="brand__mark"></span>
      <span class="brand__name">Celia Montvale, lmft</span>
    </div>
    <div class="contact-block">
      <p class="contact-name"><span class="accent">Celia Montvale,</span> LMFT</p>
      <p class="contact-line">650-381-7026 <svg class="icon"><use href="#icon-phone"/></svg></p>
      <p class="contact-line">celiamontvale.example <svg class="icon"><use href="#icon-web"/></svg></p>
      <p class="contact-line">celia@celiamontvale.example <svg class="icon"><use href="#icon-mail"/></svg></p>
    </div>
    <div class="watermark" role="img" aria-label="Faint practice watermark in the lower right corner"></div>
    <div class="base-band"></div>
  </section>

  <section class="sheet sheet--footer" aria-label="Letterhead with contact details at bottom">
    <div class="brand">
      <span class="brand__mark"></span>
      <span class="brand__name">Celia Montvale, lmft</span>
    </div>
    <div class="side-tab"></div>
    <div class="watermark" role="img" aria-label="Faint practice watermark in the lower right corner"></div>
    <div class="footer-contacts">
      <p class="contact-name"><span class="accent">Celia Montvale,</span> LMFT</p>
      <p class="item"><svg class="icon"><use href="#icon-phone"/></svg>650-381-7026</p>
      <p class="item"><svg class="icon"><use href="#icon-web"/></svg>celiamontvale.example</p>
      <p class="item"><svg class="icon"><use href="#icon-mail"/></svg>celia@celiamontvale.example</p>
    </div>
    <div class="base-band"></div>
  </section>
</body>
</html>
```